Meadowlark Counseling Partners, LLC Needs Modern Business Card Design.

We provide behavioral health services from western Kansas to eastern Kansas. There is an abundance of competition for the services we provide with our main competitor being larger and having significantly more financial resources; however, the quality of services we provide is greater and we have started to catch the attention of the State of Kansas. We had a great logo designed by ArtFolio - this will be used to build upon our brand. The logo (attached) should be used in the card development. We want something unique, modern, but also a card design that clearly states our name, contact info, provides the name and unqiue location of each clinician, etc. Rounded edges, or a unique size, just something that makes our business card stand out from others. I have also uploaded each clinician's name and their unique location and phone number.

Our idea is to have one side be black with our logo. Then, on the other side have business cards for each individual. Plus, we want one card that is "generic" with no specific clinician's name listed so that we can give clients an appointment card when they leave. Some clinicians have two locations - we're open to design and background color, but we have started going with branding colors of black, the yellow in the logo files attached, and sometimes a gray. Our new office has been decorated using this theme.

Target Market(s)

individuals and families in need of behavioral health services; potential professional referral sources; existing referral sources

Industry/Entity Type

Business

Contact Information for Business Card

I attached a Word doc that provides clinician names, credentials and location information specific to each individual.

Font styles to use
Serif

Colors
000000
fbed22
dbdbdb
9d9d9d
c3c3c3

Requirements
Must have
• 1) use of the company logo that has been attached; 2) a template that provides us space to individualize business cards for all of our clinicians; 3) should stick to the colors we are branding with: black, yellow from the logo file, maybe a gray shade and we're open to a suggestion on a shade of white.
Nice to have
• Group discussion culminated in the thought that one side would be black with just our logo - no clinician names, etc. A unique design - rounded edges, unique size, some catchy lay-out would be nice.
Should not have
• Must not be too busy. Should look "clean." The project should stick to branding colors: black, yellow (from the logo file), maybe a gray and shade of white.

```html
<!DOCTYPE html>
<html lang="en">
<head>
<meta charset="utf-8">
<title>Meadowlark Counseling Partners — Appointment Card</title>
<link rel="stylesheet" href="https://fonts.googleapis.com/css2?family=Cinzel:wght@500&family=Didact+Gothic&family=Montserrat:ital,wght@1,400&display=swap">
<style>
  :root {
    --card-black: #0e0e0e;
    --page-white: #ffffff;
    --brand-yellow: #fbbd16;
    --text-white: #f4f4f4;
  }
  * { margin: 0; padding: 0; box-sizing: border-box; }
  html, body {
    width: 1200px;
    height: 686px;
    overflow: hidden;
    background: var(--page-white);
  }
  .card {
    position: relative;
    width: 1200px;
    height: 686px;
    background: var(--card-black);
    border-radius: 40px;
    color: var(--text-white);
  }
  .tagline {
    position: absolute;
    top: 66px;
    left: 0;
    width: 100%;
    text-align: center;
    font-family: "Montserrat", sans-serif;
    font-style: italic;
    font-size: 18px;
    letter-spacing: 0.5px;
    text-transform: uppercase;
  }
  .brand-name {
    position: absolute;
    top: 250px;
    left: 0;
    width: 100%;
    text-align: center;
    font-family: "Cinzel", serif;
    font-weight: 500;
    color: var(--brand-yellow);
    font-size: 34px;
    line-height: 1.3;
    letter-spacing: 4px;
  }
  .practice-line {
    position: absolute;
    top: 467px;
    left: 232px;
    font-family: "Didact Gothic", sans-serif;
    font-size: 19px;
    text-transform: uppercase;
    letter-spacing: 0.3px;
  }
  .appointment-line {
    position: absolute;
    top: 516px;
    left: 229px;
    font-family: "Didact Gothic", sans-serif;
    font-size: 19px;
    text-transform: uppercase;
    letter-spacing: 0.3px;
    white-space: nowrap;
  }
  .blank {
    display: inline-block;
    border-bottom: 1.5px solid var(--text-white);
    height: 1px;
    vertical-align: baseline;
    margin: 0 4px;
  }
  .blank--clinician { width: 76px; }
  .blank--date { width: 156px; margin-right: 2px; }
</style>
</head>
<body>
  <main class="card">
    <p class="tagline">“Let the sun shine in.”</p>
    <h1 class="brand-name">Meadowlark<br>Counseling Partners, LLC</h1>
    <p class="practice-line">Meadowlark Counseling Partners, LLC</p>
    <p class="appointment-line">Your next appointment with<span class="blank blank--clinician"></span>has been scheduled for<span class="blank blank--date"></span>.</p>
  </main>
</body>
</html>
```